DL Flyer Needed for Legal/Conveyancing Services

Double sided DL flyer wanted -
Page 1 - advertising services of www.brookhavenlegal.com.au and http://www.brookhavenlegal.com.au/lp-v1/ (divorce, property setttlement, child custody etc)
Page 2 - advertising conveyancing services (Corinne Maltby, buying and selling houses). Our professional fees for acting on the sale of a property is $1,050 (inclusive of GST) and our price for acting on the purchase of a new property is $1,250 (inclusive of GST). Disbursements (searches and property certificates etc) are extra. Our key messages for Conveyancing are: we work with the Real Estate Agent to achieve a fast exchange and smooth settlement, Corinne Maltby has over 20 years experience, quick contract preparation, 'red alert' contract advice from $220 to give you peace of mind prior to signing.
Please see update posted to all designers.
Updates

Hi Designers, There appears to be some confusion as to which information is relevant to which side, please note the following: Side 1 - content from www.brookhavenlegal.com.au and http://www.brookhavenlegal.com.au/lp-v1/ only. Side 2 - content from the uploaded business card (see design brief) and the following: EXPERIENCE - Corinne Maltby has over 20 years’ experience in Conveyancing and is committed to making the process as fast and stress free as possible. Corinne is friendly, professional and down to earth. FAST, RELIABLE SERVICE – Corinne is available on 0461 275 938 or corinne@brookhavnlegal.com.au. COMPETITIVE PRICING – No hidden or excessive fees! Basic vendor fee is $1,050 (inclusive of GST) and basic purchaser fee is $1,250 (inclusive of GST). Our basic fee is for a standard residential sale or purchase. Our fee includes everything except our out of pocket expenses for property enquiries, search fees and certificates (disbursements). We also offer competitive pricing for; sale and purchase of strata title, old system and qualified title, community title, off the plan, subdivisions, house and land packages and commercial premises. QUICK CONTRACT REVIEW – Agent Exchange, Auction or in a hurry? no worries! Corinne is available to examine contracts at short notice and provide clients with a brief overview to alleviate any concerns they may have prior to exchange, auction or incurring pest and building report expenses. The cost of a quick contract review is from $220 (inclusive of GST) and this amount will be deducted from the total fee as per the above. LEGALLY SOUND ADVICE – Our lawyers are able to advise clients on all legal issues. Kind Regards,

```html
<!DOCTYPE html>
<html lang="en">
<head>
<meta charset="utf-8">
<title>Brookhaven Legal – DL Flyer</title>
<link rel="stylesheet" href="https://fonts.googleapis.com/css2?family=Tinos:ital,wght@0,400;0,700;1,400;1,700&family=Roboto:wght@300;400&family=Roboto+Condensed:wght@300;400&display=swap">
<style>
  :root{
    --stage:#464646;
    --paper:#ffffff;
    --ink:#1e1e1e;
    --green:#7cb53c;
    --green-dark:#4d8a1f;
    --green-head:#6aab2e;
    --blue:#286e96;
    --black:#050505;
    --mist:#f1f1f1;
    --logo-navy:#1d3a5a;
  }
  *{box-sizing:border-box;margin:0;padding:0}
  html,body{width:1200px;height:1080px;overflow:hidden;background:var(--stage)}
  .stage{position:relative;width:1200px;height:1080px}
  .flyer{position:absolute;top:113px;width:413px;height:851px;background:var(--paper);overflow:hidden}
  .flyer--front{left:163px}
  .flyer--back{left:615px}

  /* brand lockup */
  .brand{position:absolute;display:flex;align-items:center;gap:12px;
    font-family:"Tinos",serif;font-weight:400;color:var(--logo-navy);
    font-size:26px;line-height:26px;letter-spacing:1px;text-transform:uppercase;white-space:nowrap}
  .brand__dot{flex:none;width:62px;height:62px;border-radius:50%;background:var(--green)}

  /* front */
  .hero{position:absolute;left:0;top:0;width:413px;height:317px;
    background:linear-gradient(180deg,#fafafa 0%,#e9e9e9 55%,#f6f6f6 100%)}
  .flyer--front .brand{left:62px;top:38px}
  .hero__headline{position:absolute;left:20px;top:143px;width:250px;text-align:center;
    font-family:"Tinos",serif;font-variant:small-caps;font-weight:400;font-size:21px;line-height:24px;
    color:#2a2a2a;letter-spacing:.5px;white-space:nowrap}
  .hero__headline strong{font-weight:700;color:#111}
  .hero__photo{position:absolute;left:250px;top:92px;width:150px;height:225px;
    background:linear-gradient(180deg,#d8d8d8 0%,#3a3a3a 60%,#222 100%);border-radius:70px 70px 0 0}
  .promise{position:absolute;left:0;top:317px;width:413px;height:67px;
    background:linear-gradient(180deg,var(--green) 0%,var(--green-dark) 100%);
    color:#fff;text-align:center;font-family:"Roboto Condensed",sans-serif;font-weight:300;
    font-size:24px;line-height:26px;padding-top:7px}
  .why{position:absolute;left:0;top:384px;width:413px;height:180px;background:var(--blue);
    color:#eef4f8;padding:11px 32px 0 42px;font-family:"Tinos",serif}
  .why h2{font-size:15px;font-weight:700;color:#fff;margin-bottom:12px}
  .why p{font-size:13.3px;line-height:13.9px;text-align:justify}
  .specialties{position:absolute;left:0;top:564px;width:413px;height:163px;background:var(--mist)}
  .specialties h2{position:absolute;top:9px;width:100%;text-align:center;font-family:"Tinos",serif;
    font-variant:small-caps;font-weight:400;font-size:23px;color:#1a1a1a;letter-spacing:.5px}
  .specialty{position:absolute;top:47px;width:90px;text-align:center;font-family:"Tinos",serif;font-size:11px;line-height:11.5px;color:#222}
  .specialty__photo{display:block;width:70px;height:70px;border-radius:50%;margin:0 auto 6px}
  .contact{position:absolute;left:0;top:727px;width:413px;height:124px;background:var(--black);
    color:#fff;text-align:center;font-family:"Tinos",serif}
  .contact h3{font-weight:400;font-size:15px;letter-spacing:.3px;margin-top:16px;margin-bottom:11px}
  .contact p{font-size:14.5px;line-height:18.5px}

  /* back */
  .flyer--back .brand{left:72px;top:27px}
  .services{position:absolute;left:36px;top:120px;width:338px;font-family:"Tinos",serif;
    font-size:11.6px;line-height:15.3px;color:var(--ink);text-align:justify;hyphens:auto}
  .services p{margin-bottom:15.3px}
  .services .label{color:var(--green-head);font-weight:700}
  .portrait{position:absolute;left:175px;top:517px;width:238px;height:257px;
    background:radial-gradient(ellipse at 60% 32%,#d9b08f 0%,#b98d6d 26%,#cfc9cf 55%,#ffffff 85%)}
  .card{position:absolute;z-index:1;left:36px;top:560px;font-family:"Roboto",sans-serif;font-weight:300;color:#333}
  .card__name{font-size:18px;line-height:20px;color:#333}
  .card__role{font-size:12.5px;line-height:14px;margin-bottom:14px}
  .card__lines{font-size:11.6px;line-height:13.8px;margin-bottom:9px}
  .card__tag{font-size:11.6px;line-height:14px;text-transform:uppercase}
  .web-bar{position:absolute;left:0;top:774px;width:413px;height:77px;
    background:linear-gradient(180deg,var(--green) 0%,#6aa92e 100%);color:#fff;
    font-family:"Tinos",serif;font-size:28px;text-align:center;line-height:66px;white-space:nowrap}
</style>
</head>
<body>
<div class="stage">

  <section class="flyer flyer--front">
    <div class="hero">
      <div class="brand"><span class="brand__dot"></span><span>Brookhaven<br>Legal</span></div>
      <h1 class="hero__headline">You Need an<br><strong>Experienced Lawyer</strong><br>Who’ll Act in<br>Your Best Interests</h1>
      <div class="hero__photo" role="img" aria-label="Photo of a confident lawyer with arms crossed"></div>
    </div>
    <div class="promise">Get a Fast, Cost Effective<br>Solution in Your Favour</div>
    <div class="why">
      <h2>Why Choose Brookhaven Legal?</h2>
      <p>If you’re on this page it’s because you’re not looking for just any Lawyer, you’re looking for a Lawyer who is right for you“As experienced Lawyers practicing exclusively in Family and Relationship Law, we understand the challenges you’re facing and are here to help. We aim to make the process as easy as possible by offering a personalised service second-to-none. After all, when you’re dealing with intensely personal legal issues, waiting for sound legal advice is an added stress you shouldn’t have to face.</p>
    </div>
    <div class="specialties">
      <h2>Our Specialties</h2>
      <div class="specialty" style="left:28px"><span class="specialty__photo" role="img" aria-label="Photo of a smiling child" style="background:#c79a6a"></span>Child<br>Custody</div>
      <div class="specialty" style="left:118px;top:45px"><span class="specialty__photo" role="img" aria-label="Photo of hands holding a model house" style="background:#cdb9a3"></span>Property<br>Settlement</div>
      <div class="specialty" style="left:205px;top:45px"><span class="specialty__photo" role="img" aria-label="Photo of a mediation meeting at a table" style="background:#8e8e8e"></span>Mediation</div>
      <div class="specialty" style="left:292px"><span class="specialty__photo" role="img" aria-label="Photo of a mother and child" style="background:#a07c62"></span>Other<br>Family Law</div>
    </div>
    <div class="contact">
      <h3>FOR MORE INFORMATION PLEASE CONTACT</h3>
      <p>Phone: <strong>1300 618 294</strong></p>
      <p>Email: info@brookhavenlegal.com.au</p>
      <p>Website: www.brookhavenlegal.com.au</p>
    </div>
  </section>

  <section class="flyer flyer--back">
    <div class="brand"><span class="brand__dot"></span><span>Brookhaven<br>Legal</span></div>
    <div class="services">
      <p><span class="label">EXPERIENCE -</span> Corinne Maltby has over 20 years’ experience in Conveyancing and is committed to making the process as fast and stress free as possible. Corinne is friendly, professional and down to earth. FAST, RELIABLE SERVICE – Corinne is available on <strong><em>0461 275 938</em></strong> or <strong><em>corinne@brookhavnlegal.com.au.</em></strong></p>
      <p><span class="label">COMPETITIVE PRICING –</span> No hidden or excessive fees! Basic vendor fee is $1,050 (inclusive of GST) and basic purchaser fee is <strong>$1,250</strong> (inclusive of GST). Our basic fee is for a standard residential sale or purchase. Our fee includes everything except our out of pocket expenses for property enquiries, search fees and certificates (disbursements). We also offer competitive pricing for; sale and purchase of strata title, old system and qualified title, community title, off the plan, subdivisions, house and land packages and commercial premises.</p>
      <p><span class="label">QUICK CONTRACT REVIEW –</span> Agent Exchange, Auction or in a hurry? no worries! Corinne is available to examine contracts at short notice and provide clients with a brief overview to alleviate any concerns they may have prior to exchange, auction or incurring pest and building report expenses. The cost of a quick contract review is from <strong>$220</strong> (inclusive of GST) and this amount will be deducted from the total fee as per the above.</p>
      <p><span class="label">LEGALLY SOUND ADVICE –</span> Our lawyers are able to advise clients on all legal issues.</p>
    </div>
    <div class="portrait" role="img" aria-label="Portrait photo of the conveyancer"></div>
    <div class="card">
      <div class="card__name">Corinne Maltby</div>
      <div class="card__role">Property Conveyancing</div>
      <div class="card__lines">m 0461 275 938<br>t 1300 618 294<br>w brookhavenlegal.com.au<br>e corinne@brookhavenlegal.com</div>
      <div class="card__lines">Harbour Hub, 148 Mertoun Rd<br>Kelvale NSW 2291</div>
      <div class="card__tag">Competitive rates and<br>legally sound advice.</div>
    </div>
    <div class="web-bar">www.brookhavenlegal.com.au</div>
  </section>

</div>
</body>
</html>
```